Oversized Post card design

Need a post card design for rebrand, old post card attached for reference but some new content logos and colors. Id like to see new designs please use the one i posted as a reference of the type of design we like

Requirements
Must have
• Pricing page should no longer have "metered" plans only unlimited with these:
• 1 User: $29.99
• 2-10: $24.99/user
• 11-49: $21.99/user
• 50+: Contact Us!
• Add Ons:
• Call Recording: Starting at $5/user
• Additional Local Numbers: $1.99/number
• Fax to email: Starting at $8/user
• Toll Free Numbers: 1.99/number plus usage

```html
<!DOCTYPE html>
<html lang="en">
<head>
<meta charset="utf-8">
<title>Nuvolane – Plans and Pricing Postcard</title>
<link rel="stylesheet" href="https://fonts.googleapis.com/css2?family=Montserrat:wght@500;600;700&display=swap">
<style>
  :root {
    --backdrop: #ababab;
    --paper: #ffffff;
    --ink-dark: #1f1f1f;
    --brand-blue: #1592d6;
    --panel-blue: #0f98d8;
    --panel-grey: #e4e4e4;
    --purple: #6a3a9c;
    --indigo: #4a5bb4;
    --sky: #3fbdf0;
    --logo-ink: #2b2b2b;
    --stripe-grey: #8a8a8a;
  }
  html, body {
    margin: 0;
    padding: 0;
    width: 1200px;
    height: 777px;
    overflow: hidden;
    background: var(--backdrop);
    font-family: "Montserrat", sans-serif;
  }
  .postcard {
    position: absolute;
    left: 216px;
    top: 140px;
    width: 767px;
    height: 496px;
    display: block;
  }
  .headline { font-family: "Montserrat", sans-serif; font-weight: 700; fill: var(--brand-blue); font-size: 47px; letter-spacing: -0.5px; }
  .brand-name { font-family: "Montserrat", sans-serif; font-weight: 600; fill: var(--logo-ink); font-size: 32px; letter-spacing: 1px; }
  .addons-title { font-family: "Montserrat", sans-serif; font-weight: 500; fill: var(--paper); font-size: 31px; }
  .addon-item { font-family: "Montserrat", sans-serif; font-weight: 500; fill: var(--paper); font-size: 14.5px; }
  .plan-title { font-family: "Montserrat", sans-serif; font-weight: 600; fill: var(--paper); font-size: 25px; }
  .tier-cell { fill: var(--paper); }
  .tier-label { font-family: "Montserrat", sans-serif; font-weight: 600; fill: var(--ink-dark); font-size: 24px; }
  .tier-price { font-family: "Montserrat", sans-serif; font-weight: 600; fill: var(--ink-dark); font-size: 17.5px; }
  .icon { fill: none; stroke: var(--paper); stroke-width: 2; stroke-linecap: round; stroke-linejoin: round; }
</style>
</head>
<body>
<svg class="postcard" viewBox="0 0 948 613" xmlns="http://www.w3.org/2000/svg" aria-label="Nuvolane plans and pricing postcard">
  <defs>
    <linearGradient id="band-purple" x1="0" x2="1">
      <stop offset="0" stop-color="var(--purple)"/>
      <stop offset="1" stop-color="var(--indigo)"/>
    </linearGradient>
    <linearGradient id="band-indigo" x1="0" x2="1">
      <stop offset="0" stop-color="#4d55b0"/>
      <stop offset="1" stop-color="#3a86cc"/>
    </linearGradient>
    <linearGradient id="sweep-blue" x1="0" y1="0" x2="1" y2="0">
      <stop offset="0" stop-color="#5a3fa0"/>
      <stop offset="0.5" stop-color="#3b6cc0"/>
      <stop offset="1" stop-color="#2aa6e0"/>
    </linearGradient>
    <linearGradient id="corner-blue" x1="0" x2="1">
      <stop offset="0" stop-color="#5a8fd6"/>
      <stop offset="1" stop-color="var(--sky)"/>
    </linearGradient>
    <linearGradient id="strip-sky" x1="0" x2="1">
      <stop offset="0" stop-color="#9fc3ea"/>
      <stop offset="1" stop-color="#3fc6f2"/>
    </linearGradient>
  </defs>

  <!-- card base -->
  <rect class="card-base" width="948" height="613" fill="var(--paper)"/>

  <!-- header -->
  <g class="brand-top">
    <rect x="30" y="30" width="30" height="30" fill="var(--brand-blue)"/>
    <text class="brand-name" x="72" y="57">NUVOLANE</text>
  </g>
  <text class="headline" x="410" y="72">PLANS AND PRICING</text>

  <!-- upper bands -->
  <polygon class="band-sky" points="322,105 948,105 948,123 330,123" fill="url(#strip-sky)"/>
  <polygon class="band-purple" points="0,92 313,92 335,124 0,124" fill="url(#band-purple)"/>

  <!-- light grey field behind plan panel -->
  <polygon class="field-grey" points="423,124 948,124 948,459 633,459" fill="var(--panel-grey)"/>

  <!-- diagonal sweep -->
  <polygon class="sweep" points="270,124 420,124 635,459 470,459" fill="url(#sweep-blue)"/>
  <polygon class="sweep-light" points="380,124 423,124 633,459 590,459" fill="#6f8fd0" opacity="0.7"/>
  <polygon class="stripe-grey" points="232,124 248,124 463,459 447,459" fill="var(--stripe-grey)"/>
  <polygon class="stripe-white" points="248,124 262,124 477,459 463,459" fill="var(--paper)"/>

  <!-- add-ons panel -->
  <polygon class="addons-panel" points="0,124 232,124 447,459 0,459" fill="var(--ink-dark)"/>
  <polygon class="band-indigo" points="0,139 425,139 433,169 0,169" fill="url(#band-indigo)"/>

  <text class="addons-title" x="56" y="225">ADD ONS</text>

  <g class="addon">
    <g class="icon" transform="translate(38,253)">
      <rect x="4" y="0" width="8" height="14" rx="4"/>
      <path d="M1 9 a7 7 0 0 0 14 0 M8 16 v5 M4 22 h8"/>
    </g>
    <text class="addon-item" x="63" y="271">Call Recording: Starting at $5/user</text>
  </g>
  <g class="addon">
    <g class="icon" transform="translate(36,296)">
      <path d="M4 1 l4 0 l2 6 l-3 2 q2 5 6 8 l3 -3 l5 2 l0 4 q-2 3 -6 2 q-12 -5 -15 -17 q0 -3 4 -4z"/>
    </g>
    <text class="addon-item" x="66" y="312">Additional Local Numbers: $1.99/number</text>
  </g>
  <g class="addon">
    <g class="icon" transform="translate(35,341)">
      <rect x="0" y="4" width="24" height="18"/>
      <path d="M0 22 l9 -8 M24 22 l-9 -8 M0 4 l12 9 l12 -9"/>
      <circle cx="12" cy="7" r="4"/>
    </g>
    <text class="addon-item" x="68" y="357">Fax to email: Starting at $8/user</text>
  </g>
  <g class="addon">
    <g class="icon" transform="translate(35,383)">
      <rect x="0" y="0" width="16" height="30" rx="2"/>
      <path d="M0 5 h16 M0 24 h16"/>
    </g>
    <text class="addon-item" x="68" y="401">Toll Free Numbers: 1.99/number plus usage</text>
  </g>

  <!-- plan panel -->
  <polygon class="plan-panel" points="475,154 925,154 925,431 653,431" fill="var(--panel-blue)"/>
  <text class="plan-title" x="533" y="196">Unlimited Seat</text>

  <g class="tier">
    <rect class="tier-cell" x="663" y="211" width="104" height="42"/>
    <text class="tier-label" x="715" y="241" text-anchor="middle">1 User</text>
    <rect class="tier-cell" x="787" y="211" width="122" height="42"/>
    <text class="tier-price" x="848" y="242" text-anchor="middle">$29.99</text>
  </g>
  <g class="tier">
    <rect class="tier-cell" x="663" y="264" width="104" height="43"/>
    <text class="tier-label" x="715" y="295" text-anchor="middle">2-10</text>
    <rect class="tier-cell" x="787" y="264" width="122" height="43"/>
    <text class="tier-price" x="848" y="292" text-anchor="middle">$24.99/user</text>
  </g>
  <g class="tier">
    <rect class="tier-cell" x="663" y="318" width="104" height="43"/>
    <text class="tier-label" x="715" y="350" text-anchor="middle">11-49</text>
    <rect class="tier-cell" x="787" y="318" width="122" height="43"/>
    <text class="tier-price" x="848" y="346" text-anchor="middle">$21.99/user</text>
  </g>
  <g class="tier">
    <rect class="tier-cell" x="663" y="370" width="104" height="43"/>
    <text class="tier-label" x="715" y="401" text-anchor="middle">50+</text>
    <rect class="tier-cell" x="787" y="370" width="122" height="43"/>
    <text class="tier-price" x="848" y="398" text-anchor="middle">Contact Us!</text>
  </g>

  <!-- footer -->
  <rect class="band-footer" x="0" y="459" width="600" height="16" fill="url(#band-purple)"/>
  <polygon class="footer-corner" points="568,459 948,459 948,613 663,613 578,475 578,459" fill="url(#corner-blue)"/>
  <text class="headline" x="77" y="557">PLANS AND PRICING</text>
  <g class="brand-bottom">
    <rect x="690" y="516" width="30" height="30" fill="var(--logo-ink)"/>
    <text class="brand-name" x="732" y="543">NUVOLANE</text>
  </g>
</svg>
</body>
</html>
```